Calorie website redesign while keeping current structure

****UPDATE****
Dear designers!

I'd really appreciate to see new color ideas.
The green-red-yellow scheme is the old scheme, and I want to change it. I asked for new colors with same structure, but I get designs with old colors and new structure. :(

My goal is to get a design with a good overall impression.
I need new color ideas where colors are in harmony and gives pleasant OVERALL impression to the eyes.

Your tools again:
1. you can use any colors (i prefer green and blue variations as the most dominant color)
2. you can use gradients
3. you can use transparency.
4. you can use background images.
5. you can change font type (but stay compatible with other languages like Hungarian)

All designs I got so far was not usable because they were not compatible with the site structure.
It was written in description we have fixed sizes, and what you can change and what you CANT change.

Note: i dont like white color. It looks empty and it doesnt give a character to the site.

Separation: it's important the site parts to be easily separated by the eye. The site consists of 4 main parts: menu, what did you eat, what did you do, and yellow calculation boxes. They should be separated easily by looking at it.
*****END OF UPDATE****

DEAR DESIGNERS!

My name is Zsolt, I run this website tornelviqa.hu which is the most popular calorie counting website in Hungary with 500.000 users. It has also an English version, fendrowix.com (started not long ago). Now you have to focus only on the mobile version main page:
https://fendrowix.com/?layout=m

There a lot of other urgent tasks about the site and I had no chance to improve the design in the last years . But I'm aware of the problem: the website doesn't look good enough to be appealing for new users. So now I decided to run a contest to see if you can help me with this.

UNDERSTANDING CURRENT DESIGN CONCEPT:

1. The original concept of the site was that calories are "bad" so they are red color, and sport activites are "good", so they are green color. Red and green is very different color (which is advantage in separating those sections), but they don't look nice together, so I'm ready to change the colors but somehow we still need to show that calories are "bad" and sports are "good". The yellow boxes are showing calculated numbers.
2. The original concept was that I wanted the whole site to have a "calculator feeling": the message is that it is not made to attract people by fancy design, but it's strongness is it's knowledge and usability, same as a hand calculator. I want to maintain this concept, but with a more modern design.
3. Another concept is that I want to make the usability easier for long time users instead of first time users. It means I prefer to show more options/buttons on the screen (which can be frightening to new users, but it's okay), instead of having a very easy-to-use feeling when you first visit our site (but later you need to click a lot to reach functions). Number one priority is still long time usability.
4. I want to emphasise I love to use colors to separate parts.

SUMMARY:

i know it's not easy to make it look better AND compatible current structure, it's a big challenge. Be creative and use your imaginations. It's possible that I will need further adjustments from winning designer in the future, so it's a plus if you will be available to work.

Thanks,
Zsolt Benkő
Updates

I got a car accident, and couldnt leave the countryside. i cant view and review works from here. I will send u an image tomorrow afternoon showing the fixed structure, to avoid misunderstandings in future. so far none of the design is usable, because they were NOT created in our 40px size/5px space structure as i requested in posting thanks for understanding

Received designs were not compatible with structure. It was written in the description, but now I also I updated the description to give a more clear view what I need.

Target Market(s)

weight-loss

Industry/Entity Type

Weight

Number of Pages Required

1 page

Font styles to use
Sans Serif

Colors

Designer to choose colors to be used in the design.

Requirements
Must have
• WHAT CHANGES AM I EXPECTING FROM YOU?
• 1. you can use new colors totally freely along all site.
• 2. You can add some color overlays, gradients, backgrounds, to different sections.
• 3. You can add new edges (delete /increase edges) to buttons/rows (without changing the size).
• 6. If you use new font, then it should be 100% compatible with different languages (for example: Hungarian characters like ö, ő, ü, ű, etc).
• 2. I need better design for input fields (currently inactive is red, and active is white, but you can change it)
• OTHER IMPORTANT NOTES:
• 1. Be careful with technologies which could cause performance issues, as site speed is very important.
• 2. The main goal now is NOT to get new images on buttons (it's perfectly okay if you dont touch them), but an overall better and consistent look. However if you want to achieve this goal by also redesigning buttons and rows (new color, new active/press effect, ), you can do this too. In current version buttons are 40x40, but in new design they will be 80x80.
• 3. The new color concept needs to be compatible with meal colors like breakfast, dinner, etc.
• 4. I love flat design, but I want to encourage you not to limit your imagination. I really appreciate creative ideas, flat or not.
• 5. I want a mobil app athmosphere. Most of the similar sites use so simple designs that they look like settings menu of your phone. I find them very boring, I want to separate sections with nice colors (maybe backgrounds).
• 6. Clear visibility is also important so try to avoid hurting it with too many new design elements.
• 7. First I need only a picture about the new design showing the main page with added meal rows. But of course in the end I need the winning design in a format which I we can use also to sub-menus and desktop version of the site.
Should not have
• WHAT YOU SHOULD NOT CHANGE:
• The menu structure, positions, the buttons sizes. The button animations and sub-menus are all based on this structure, where we use 5px spacing, and 40px rows, and buttons (however we want to double the resolution for these ones: 10 and 80px). We cannot change this basic structure, because it needs a lot of programming, so you need to be creative to make it look better with current structure.

```html
<!DOCTYPE html>
<html lang="en">
<head>
<meta charset="utf-8">
<title>Fendrowix – mobile main page row concepts</title>
<link href="https://fonts.googleapis.com/css2?family=Roboto:wght@300;400;500&display=swap" rel="stylesheet">
<style>
:root{
  --ink:#5f6266;
  --slate:#2a3240;
  --slate-cell:#343d4d;
  --night:#151a21;
  --charcoal:#24272b;
  --grey-cell:#9ea2a8;
  --grey-chip:#8e9399;
  --pale:#dfe4ea;
  --pale-btn:#cfe3f8;
  --mint:#0fd190;
  --mint-soft:#8ee8c6;
  --leaf:#08de72;
  --sky:#0a84f0;
  --sky-soft:#5bb8f5;
  --peach:#ffd4a0;
  --rose:#f9c3d9;
  --coral:#f9a9a3;
  --lilac:#c7b0f5;
  --amber:#ff9500;
  --violet:#7e57e8;
  --crimson:#e8101e;
  --wine:#a3001a;
  --gold:#c9a227;
  --forest:#1f5e2e;
  --alert:#e3262e;
}
*{box-sizing:border-box;margin:0;padding:0}
html,body{width:1200px;height:994px;overflow:hidden;background:#fff}
body{font-family:"Roboto",Arial,sans-serif;color:#fff}
.stage{position:absolute;left:0;top:0;width:2100px;height:1740px;transform:scale(.5714);transform-origin:0 0}
.label{position:absolute;font-size:112px;font-weight:300;color:var(--ink);line-height:1;letter-spacing:-2px}
.abs{position:absolute}

/* ---------- generic row parts ---------- */
.row{position:absolute;left:0;right:0;height:57px}
.cell{position:absolute;top:0;height:57px}
.food{background:var(--slate-cell);border-bottom:5px solid var(--line,transparent)}
.food .name{position:absolute;left:20px;top:9px;font-size:20px;font-weight:300}
.food .qty{position:absolute;left:20px;top:32px;font-size:15px;font-weight:300;opacity:.75}
.kcal{position:absolute;right:8px;top:4px;font-size:26px;font-weight:400;text-align:right;line-height:1}
.kcal small{display:block;font-size:14px;font-weight:300;margin-top:3px;opacity:.85}
.meal{background:var(--tag);}
.meal .name{position:absolute;left:16px;top:16px;font-size:20px;font-weight:500}
.slot{background:var(--charcoal)}
.macros{position:absolute;top:0;width:58px;height:57px}
.macros i{display:flex;align-items:center;height:19px;font-style:normal}
.macros s{text-decoration:none;display:block;height:14px;line-height:14px;font-size:10px;padding-left:3px;color:#0c1a10}
.macros .p s{width:20px;background:var(--leaf)}
.macros .c s{width:38px;background:var(--amber);border-radius:0 7px 7px 0}
.macros .f s{width:20px;background:var(--violet);color:#fff}
.macros b{margin-left:auto;padding-right:3px;font-size:12px;font-weight:500}
.more{position:absolute;top:0;width:58px;height:57px;background:var(--slate);display:flex;align-items:center;justify-content:center;font-size:20px;letter-spacing:2px;font-weight:700}

/* ---------- panel #1 / #2b (dark slate) ---------- */
.slate-panel{position:absolute;width:453px;background:var(--slate);border:4px solid #1b2029}
.slate-panel .cell.food,.slate-panel .cell.blank{left:5px;width:312px}
.slate-panel .blank{background:#232a36}
.slate-panel .meal{left:115px;width:202px}
.slate-panel .macros{left:322px}
.slate-panel .more{left:387px;background:#262d39}

/* ---------- panel #2 (grey concept) ---------- */
.grey-panel{position:absolute;left:217px;top:60px;width:453px;height:1575px;background:var(--charcoal)}
.grey-panel .food{background:var(--grey-cell)}
.grey-panel .cell.food{left:7px;width:311px}
.grey-panel .slot{left:7px;width:101px}
.grey-panel .meal{left:116px;width:202px;background:var(--tag)}
.grey-panel .macros{left:324px;opacity:.55}
.grey-panel .more{left:389px;width:56px;background:var(--grey-cell)}

.topbar{position:absolute;left:0;top:0;width:447px;height:55px;background:linear-gradient(90deg,#1d5a2c,#2f7a3c 55%,#1d5a2c)}
.brand{position:absolute;display:flex;align-items:center;gap:8px;font-size:15px;font-weight:500}
.brand .dot{width:26px;height:26px;border-radius:50%;background:var(--crimson)}
.hamb{position:absolute;width:48px;height:26px;border-top:5px solid #fff;border-bottom:5px solid #fff}
.hamb::after{content:"";position:absolute;left:0;right:0;top:6px;height:5px;background:#fff}

.subbar{position:absolute;left:0;top:77px;width:453px;height:63px;background:#0b2a4a}
.subbar .seg{position:absolute;top:3px;height:57px}
.letter{display:inline-flex;width:20px;height:20px;border-radius:50%;background:rgba(255,255,255,.4);align-items:center;justify-content:center;font-size:12px;margin:0 10px}

.navbar{position:absolute;left:0;top:142px;width:453px;height:66px;background:#4a4e54}
.navbar .btn{position:absolute;top:5px;height:56px;background:var(--grey-cell);display:flex;align-items:center;justify-content:center;color:#7fb2f0;font-size:30px;font-weight:300}
.today{font-size:26px;color:#fff;font-weight:300}

.progress{position:absolute;background:var(--night)}
.progress .num{position:absolute;font-size:26px;font-weight:400;color:#fff}
.progress .num em{font-style:normal;color:var(--mint)}
.progress .msg{font-size:13px;color:#d7dbe0;margin-left:6px}
.progress .msg em{font-style:normal;color:var(--mint)}
.gear{position:absolute;width:28px;height:28px}

.search{position:absolute;left:7px;top:278px;width:374px;height:57px;background:#fff;border-radius:29px;color:#b5b9be;font-size:20px;font-weight:300}
.search .go{position:absolute;right:5px;top:6px;width:45px;height:45px;border-radius:50%;background:#5fe0b7}
.chip{position:absolute;width:82px;height:27px;background:var(--grey-chip);font-size:10px;color:#d8dbe0;display:flex;align-items:center;justify-content:center}

.total{background:var(--grey-cell)}
.total .name{position:absolute;left:35px;top:18px;font-size:19px;font-weight:500}
.total::before{content:"";position:absolute;left:0;top:0;border-left:20px solid var(--mint-soft);border-top:28px solid transparent;border-bottom:29px solid transparent}
.round{border-radius:50%}

.burn{position:absolute;left:0;top:1305px;width:453px;height:270px;background:#c9ced5}
.burn .cell{background:var(--pale);left:7px;width:374px}
.burn .more{background:var(--pale-btn);left:389px;width:56px}
.burn .name,.burn .qty,.burn .kcal{color:#fff}

/* ---------- #2a bars ---------- */
.stack{position:absolute}
.vert{position:absolute;display:flex;flex-direction:column;align-items:center;font-size:11px;line-height:12px;font-weight:500}
.shadow{text-shadow:0 1px 2px #000}

.act{position:absolute;top:0;height:57px;display:flex;align-items:center;justify-content:center}
.arrow{position:absolute;height:2px;background:var(--alert)}
</style>
</head>
<body>
<svg width="0" height="0" style="position:absolute">
  <symbol id="cog" viewBox="0 0 24 24">
    <path fill="currentColor" d="M10.3 1h3.4l.5 3a8 8 0 0 1 2.2 1.3l2.9-1.1 1.7 3-2.3 1.9a8 8 0 0 1 0 2.6l2.3 1.9-1.7 3-2.9-1.1a8 8 0 0 1-2.2 1.3l-.5 3h-3.4l-.5-3a8 8 0 0 1-2.2-1.3l-2.9 1.1-1.7-3 2.3-1.9a8 8 0 0 1 0-2.6L3 7.2l1.7-3 2.9 1.1A8 8 0 0 1 9.8 4zM12 8.2a3.8 3.8 0 1 0 0 7.6 3.8 3.8 0 0 0 0-7.6z"/>
  </symbol>
</svg>

<main class="stage">
  <div class="label" style="left:60px;top:140px">#2</div>
  <div class="label" style="left:812px;top:22px">#2a</div>
  <div class="label" style="left:1268px;top:140px">#1</div>
  <div class="label" style="left:812px;top:895px">#2b</div>

  <!-- ================= concept #2 : full page ================= -->
  <section class="grey-panel">
    <header class="topbar">
      <div class="brand" style="left:12px;top:14px"><span class="dot"></span>Tornelviqa</div>
      <div class="abs" style="left:122px;top:0;width:6px;height:55px;background:#174a24"></div>
      <div class="abs" style="left:145px;top:16px;font-size:22px">torne…</div>
      <div class="abs" style="left:226px;top:18px;width:14px;height:18px;background:#e8e8e8;border-radius:3px"></div>
      <div class="abs" style="left:252px;top:16px;width:20px;height:20px;background:#fff;border:2px solid #2a6bb8"></div>
      <div class="abs round" style="left:282px;top:16px;width:24px;height:24px;background:#ddd"></div>
      <div class="abs" style="left:316px;top:0;width:6px;height:55px;background:#174a24"></div>
      <div class="hamb" style="left:356px;top:15px"></div>
    </header>

    <div class="subbar">
      <div class="seg" style="left:0;width:126px;background:#8cc4ee">
        <div class="brand" style="left:10px;top:16px;font-size:13px;font-weight:400"><span class="dot" style="background:#e6f2fb"></span>Fendrowix</div>
      </div>
      <div class="seg" style="left:133px;width:184px;background:#6cb2ef;display:flex;align-items:center;justify-content:center"><span class="letter">a</span><span class="letter">b</span><span class="letter">c</span></div>
      <div class="seg" style="left:324px;width:129px;background:#8cc4ee">
        <div class="abs" style="left:88px;top:20px;width:24px;height:18px;border-top:1px solid #fff;border-bottom:1px solid #fff"></div>
        <div class="abs" style="left:88px;top:29px;width:24px;height:1px;background:#fff"></div>
      </div>
    </div>

    <nav class="navbar">
      <div class="btn" style="left:5px;width:58px">‹</div>
      <div class="btn" style="left:70px;width:311px"><span class="today">Today</span>
        <span class="abs" style="left:263px;top:17px;width:20px;height:20px;border:2px solid #fff;border-radius:3px"></span></div>
      <div class="btn" style="left:388px;width:57px">›</div>
    </nav>

    <div class="progress" style="left:0;top:217px;width:453px;height:53px">
      <div class="num" style="left:8px;top:8px"><em>1500</em>/2500<span class="msg">you can eat <em>1000</em> more kcal today</span></div>
      <svg class="gear" style="left:408px;top:8px;color:#8d9298"><use href="#cog"/></svg>
      <div class="abs" style="left:5px;top:43px;width:440px;height:8px;background:#3a3e44;border-radius:4px"></div>
      <div class="abs" style="left:5px;top:43px;width:298px;height:8px;background:var(--forest);border-radius:4px"></div>
    </div>

    <div class="search">
      <span class="abs" style="left:18px;top:20px;width:18px;height:10px;border:2px solid #c4c7cc;border-radius:8px 8px 0 0"></span>
      <span class="abs" style="left:46px;top:15px">What did you eat?</span>
      <span class="abs" style="left:298px;top:20px;width:16px;height:16px;border-left:2px solid #c4c7cc;border-top:2px solid #c4c7cc"></span>
      <span class="go"></span>
    </div>
    <div class="more" style="left:389px;top:278px;width:56px;background:var(--grey-cell)">•••</div>

    <div class="chip" style="left:7px;top:343px">White bread</div>
    <div class="chip" style="left:95px;top:343px">Tomatoes</div>
    <div class="chip" style="left:185px;top:343px">Apples</div>
    <div class="chip" style="left:275px;top:343px">Grapes</div>
    <div class="chip" style="left:365px;top:343px">Potato</div>
    <div class="chip" style="left:7px;top:378px">Corn</div>
    <div class="chip" style="left:95px;top:378px">Pasta</div>
    <div class="chip" style="left:185px;top:378px">Protein bar</div>
    <div class="chip" style="left:275px;top:378px">Black beans...</div>
    <div class="chip" style="left:365px;top:378px">Egg</div>

    <div class="row" style="top:415px"><div class="cell food" style="--line:var(--sky-soft)"><span class="name">Cheese Sandwich</span><span class="qty">300 gr</span><span class="kcal">460<small>kcal</small></span></div>
      <div class="macros"><i class="p"><s>P:</s><b>10</b></i><i class="c"><s>C:</s><b>50</b></i><i class="f"><s>F:</s><b>35</b></i></div><div class="more">•••</div></div>
    <div class="row" style="top:479px"><div class="cell slot"></div><div class="cell meal" style="--tag:var(--sky-soft)"><span class="name">Breakfast</span><span class="kcal">460<small>kcal</small></span></div>
      <div class="macros"><i class="p"><s>P:</s><b>10</b></i><i class="c"><s>C:</s><b>50</b></i><i class="f"><s>F:</s><b>35</b></i></div><div class="more">•••</div></div>
    <div class="row" style="top:542px"><div class="cell food" style="--line:var(--mint-soft)"><span class="name">Apple</span><span class="qty">150 gr</span><span class="kcal">60<small>kcal</small></span></div>
      <div class="macros"><i class="p"><s>P:</s><b>10</b></i><i class="c"><s>C:</s><b>50</b></i><i class="f"><s>F:</s><b>35</b></i></div><div class="more">•••</div></div>
    <div class="row" style="top:606px"><div class="cell slot"></div><div class="cell meal" style="--tag:var(--mint-soft)"><span class="name">Mid-morning</span><span class="kcal">60<small>kcal</small></span></div>
      <div class="macros"><i class="p"><s>P:</s><b>10</b></i><i class="c"><s>C:</s><b>50</b></i><i class="f"><s>F:</s><b>35</b></i></div><div class="more">•••</div></div>
    <div class="row" style="top:670px"><div class="cell food" style="--line:var(--peach)"><span class="name">Cesar Salad</span><span class="qty">300 gr</span><span class="kcal">150<small>kcal</small></span></div>
      <div class="macros"><i class="p"><s>P:</s><b>10</b></i><i class="c"><s>C:</s><b>50</b></i><i class="f"><s>F:</s><b>35</b></i></div><div class="more">•••</div></div>
    <div class="row" style="top:733px"><div class="cell slot"></div><div class="cell meal" style="--tag:var(--peach)"><span class="name">Lunch</span><span class="kcal">150<small>kcal</small></span></div>
      <div class="macros"><i class="p"><s>P:</s><b>10</b></i><i class="c"><s>C:</s><b>50</b></i><i class="f"><s>F:</s><b>35</b></i></div><div class="more">•••</div></div>
    <div class="row" style="top:797px"><div class="cell food" style="--line:var(--rose)"><span class="name">Grapes</span><span class="qty">200 gr</span><span class="kcal">130<small>kcal</small></span></div>
      <div class="macros"><i class="p"><s>P:</s><b>10</b></i><i class="c"><s>C:</s><b>50</b></i><i class="f"><s>F:</s><b>35</b></i></div><div class="more">•••</div></div>
    <div class="row" style="top:861px"><div class="cell slot" style="background:var(--grey-cell)"></div><div class="cell meal" style="--tag:var(--rose)"><span class="name">Mid-afternoon</span><span class="kcal">130<small>kcal</small></span></div>
      <div class="macros"><i class="p"><s>P:</s><b>10</b></i><i class="c"><s>C:</s><b>50</b></i><i class="f"><s>F:</s><b>35</b></i></div><div class="more">•••</div></div>
    <div class="row" style="top:925px"><div class="cell food" style="--line:#b7473f"><span class="name" style="color:#9ea2a8">Pizza</span><span class="qty" style="color:#9ea2a8">300 gr</span><span class="kcal">500<small>kcal</small></span></div>
      <div class="cell slot" style="height:52px;background:var(--charcoal);opacity:.9"></div>
      <span class="abs" style="left:27px;top:9px;font-size:20px;font-weight:300;color:#8f9399">Pizza</span><span class="abs" style="left:27px;top:32px;font-size:15px;font-weight:300;color:#6f7379">300 gr</span>
      <div class="macros"><i class="p"><s>P:</s><b>10</b></i><i class="c"><s>C:</s><b>50</b></i><i class="f"><s>F:</s><b>35</b></i></div><div class="more">•••</div></div>
    <div class="row" style="top:988px"><div class="cell slot" style="background:var(--grey-cell)"></div><div class="cell meal" style="--tag:var(--coral)"><span class="name">Dinner</span><span class="kcal">500<small>kcal</small></span></div>
      <div class="macros"><i class="p"><s>P:</s><b>10</b></i><i class="c"><s>C:</s><b>50</b></i><i class="f"><s>F:</s><b>35</b></i></div><div class="more">•••</div></div>
    <div class="row" style="top:1052px"><div class="cell food" style="--line:var(--lilac)"><span class="kcal">50<small>kcal</small></span></div>
      <div class="cell slot" style="height:52px"></div>
      <span class="abs" style="left:27px;top:9px;font-size:20px;font-weight:300">Cheese Sandwich</span><span class="abs" style="left:27px;top:32px;font-size:15px;font-weight:300;opacity:.6">300 gr</span>
      <div class="macros"><i class="p"><s>P:</s><b>10</b></i><i class="c"><s>C:</s><b>50</b></i><i class="f"><s>F:</s><b>35</b></i></div><div class="more">•••</div></div>
    <div class="row" style="top:1116px"><div class="cell food" style="--line:var(--lilac)"><span class="name">Cheese Sandwich</span><span class="qty">300 gr</span><span class="kcal">50<small>kcal</small></span></div>
      <div class="macros"><i class="p"><s>P:</s><b>10</b></i><i class="c"><s>C:</s><b>50</b></i><i class="f"><s>F:</s><b>35</b></i></div><div class="more">•••</div></div>
    <div class="row" style="top:1180px"><div class="cell slot"></div><div class="cell meal" style="--tag:var(--lilac)"><span class="name">Snack</span><span class="kcal">100<small>kcal</small></span></div>
      <div class="macros"><i class="p"><s>P:</s><b>10</b></i><i class="c"><s>C:</s><b>50</b></i><i class="f"><s>F:</s><b>35</b></i></div><div class="more">•••</div></div>
    <div class="row" style="top:1243px"><div class="cell food total" style="left:7px;width:311px"><span class="name">TOTAL KCAL</span><span class="kcal" style="font-size:36px">1500<small>kcal</small></span></div>
      <div class="macros"><i class="p"><s>P:</s><b>10</b></i><i class="c"><s>C:</s><b>50</b></i><i class="f"><s>F:</s><b>35</b></i></div><div class="more round">•••</div></div>

    <div class="burn">
      <div class="search" style="top:5px;opacity:.9"><span class="abs" style="left:16px;top:15px;color:#e3e6ea">⊶ What did you do?</span><span class="go" style="background:#d6e9fb"></span></div>
      <div class="more" style="top:5px;background:var(--pale-btn)">•••</div>
      <div class="row" style="top:72px"><div class="cell food"><span class="name">Running</span><span class="qty">15 min</span><span class="kcal">350<small>kcal</small></span></div><div class="more">•••</div></div>
      <div class="row" style="top:136px"><div class="cell food"><span class="name">Riding bike</span><span class="qty">30 min</span><span class="kcal">450<small>kcal</small></span></div><div class="more">•••</div></div>
      <div class="row" style="top:200px"><div class="cell food total" style="background:var(--pale)"><span class="name">TOTAL KCAL BURN</span><span class="kcal" style="font-size:36px">1500<small>kcal</small></span></div><div class="more">•••</div></div>
    </div>
  </section>

  <!-- ================= concept #2a : summary bars ================= -->
  <div class="progress" style="left:697px;top:145px;width:453px;height:61px">
    <div class="num" style="left:6px;top:8px"><em>1500</em>/2500<span class="msg">you can eat <em>1000</em> more kcal today</span></div>
    <svg class="gear" style="left:406px;top:8px;color:#fff"><use href="#cog"/></svg>
    <div class="abs" style="left:3px;top:44px;width:446px;height:12px;background:#3b4048;border-radius:6px"></div>
    <div class="abs" style="left:3px;top:44px;width:300px;height:12px;background:var(--mint);border-radius:6px"></div>
  </div>
  <div class="abs" style="left:921px;top:237px;width:2px;height:38px;background:var(--alert)"></div>
  <div class="abs" style="left:916px;top:272px;border-left:6px solid transparent;border-right:6px solid transparent;border-top:8px solid var(--alert)"></div>

  <div class="progress" style="left:697px;top:327px;width:453px;height:61px">
    <div class="abs" style="left:4px;top:4px;width:302px;height:53px;background:var(--mint)"></div>
    <div class="abs" style="left:170px;top:8px;font-size:24px">1500/2500</div>
    <div class="abs" style="left:134px;top:37px;font-size:13px">you can eat 1000 more kcal today</div>
    <svg class="gear" style="left:406px;top:8px;color:#fff"><use href="#cog"/></svg>
  </div>

  <div class="stack" style="left:697px;top:434px;width:453px;height:138px;background:#222">
    <div class="abs" style="left:0;top:0;width:193px;height:44px;background:#1599b8"></div>
    <div class="abs" style="left:0;top:44px;width:193px;height:55px;background:#cc9118"></div>
    <div class="abs" style="left:0;top:99px;width:193px;height:39px;background:#cf0fb5"></div>
    <div class="abs" style="left:193px;top:0;width:42px;height:5px;background:#1599b8"></div>
    <div class="abs" style="left:193px;top:5px;width:42px;height:94px;background:#cc9118"></div>
    <div class="abs" style="left:193px;top:99px;width:42px;height:39px;background:#cf0fb5"></div>
    <div class="vert" style="left:92px;top:4px;color:#fff"><span>K</span><span>I</span><span>N</span><span>A</span><span>I</span><span style="margin-top:18px">K</span></div>
    <div class="vert" style="left:207px;top:4px;color:#222"><span>G</span><span>R</span><span>A</span><span>N</span><span>D</span><span>E</span><span>S</span></div>
    <div class="abs shadow" style="left:172px;top:88px;font-size:22px">1083 / 2104</div>
    <div class="abs shadow" style="left:96px;top:112px;font-size:22px">Még 1021 kcal-t ehetsz ma.</div>
    <svg class="gear" style="left:402px;top:96px;color:#fff"><use href="#cog"/></svg>
  </div>

  <div class="stack" style="left:697px;top:630px;width:453px;height:130px;background:#141b24">
    <div class="abs" style="left:3px;top:4px;width:193px;height:28px;background:var(--leaf)"></div>
    <div class="abs" style="left:3px;top:32px;width:193px;height:56px;background:var(--amber)"></div>
    <div class="abs" style="left:3px;top:88px;width:193px;height:38px;background:var(--violet)"></div>
    <div class="abs" style="left:196px;top:4px;width:40px;height:21px;background:var(--leaf)"></div>
    <div class="abs" style="left:196px;top:25px;width:40px;height:35px;background:var(--amber)"></div>
    <div class="abs" style="left:196px;top:60px;width:40px;height:66px;background:var(--violet)"></div>
    <div class="vert" style="left:86px;top:16px;color:#fff;line-height:15px"><span>K</span><span>I</span><span>N</span><span>A</span><span>I</span><span>K</span></div>
    <div class="vert" style="left:211px;top:8px;color:#fff;font-size:8px;line-height:9px"><span>G</span><span>R</span><span>A</span><span>N</span><span>D</span><span>E</span><span>S</span></div>
    <div class="abs" style="left:166px;top:76px;font-size:24px">1500/2500</div>
    <div class="abs" style="left:130px;top:105px;font-size:13px">you can eat 1000 more kcal today</div>
    <svg class="gear" style="left:406px;top:76px;color:#fff"><use href="#cog"/></svg>
  </div>

  <!-- ================= concept #1 : dark slate rows ================= -->
  <section class="slate-panel" style="left:1435px;top:136px;height:319px">
    <div class="row" style="top:0"><div class="cell food" style="--line:var(--sky)"><span class="name">Cheese Sandwich</span><span class="qty">300 gr</span><span class="kcal">460<small>kcal</small></span></div>
      <div class="macros"><i class="p"><s>P:</s><b>10</b></i><i class="c"><s>C:</s><b>50</b></i><i class="f"><s>F:</s><b>35</b></i></div><div class="more">•••</div></div>
    <div class="row" style="top:64px"><div class="cell blank"></div><div class="cell meal" style="--tag:var(--sky)"><span class="name">Breakfast</span><span class="kcal">460<small>kcal</small></span></div>
      <div class="macros"><i class="p"><s>P:</s><b>10</b></i><i class="c"><s>C:</s><b>50</b></i><i class="f"><s>F:</s><b>35</b></i></div><div class="more">•••</div></div>
    <div class="row" style="top:128px"><div class="cell food" style="--line:var(--mint)"><span class="name">Apple</span><span class="qty">150 gr</span>
        <span class="abs" style="right:6px;top:6px;font-size:24px">60 <small style="font-size:14px;font-weight:300">kcal</small></span>
        <span class="abs" style="left:214px;top:34px;width:96px;height:14px;border:1px dashed #8b95a6;font-size:10px;color:#b9c1cc;text-align:center;line-height:12px">Extra space</span>
        <span class="arrow" style="left:144px;top:35px;width:38px"></span>
        <span class="abs" style="left:180px;top:31px;border-top:5px solid transparent;border-bottom:5px solid transparent;border-left:7px solid var(--alert)"></span></div>
      <div class="macros"><i class="p"><s>P:</s><b>10</b></i><i class="c"><s>C:</s><b>50</b></i><i class="f"><s>F:</s><b>35</b></i></div><div class="more">•••</div></div>
    <div class="row" style="top:192px"><div class="cell blank"></div><div class="cell meal" style="--tag:var(--mint)"><span class="name">Mid-morning</span><span class="kcal">60<small>kcal</small></span></div>
      <div class="macros"><i class="p"><s>P:</s><b>10</b></i><i class="c"><s>C:</s><b>50</b></i><i class="f"><s>F:</s><b>35</b></i></div><div class="more">•••</div></div>
    <div class="row" style="top:256px"><div class="cell food" style="--line:var(--amber)"><span class="name">Cesar Salad</span><span class="qty">300 gr</span><span class="kcal">150<small>kcal</small></span></div>
      <div class="macros"><i class="p"><s>P:</s><b>10</b></i><i class="c"><s>C:</s><b>50</b></i><i class="f"><s>F:</s><b>35</b></i></div><div class="more">•••</div></div>
  </section>

  <!-- ================= concept #2b : row actions ================= -->
  <section class="slate-panel" style="left:702px;top:1035px;height:317px">
    <div class="row" style="top:0"><div class="cell food" style="--line:var(--sky)"><span class="name">Cheese Sandwich</span><span class="qty">300 gr</span><span class="kcal">460<small>kcal</small></span></div>
      <div class="macros"><i class="p"><s>P:</s><b>10</b></i><i class="c"><s>C:</s><b>50</b></i><i class="f"><s>F:</s><b>35</b></i></div><div class="more">•••</div></div>
    <div class="row" style="top:64px"><div class="cell blank"></div>
      <div class="cell meal" style="--tag:var(--sky);width:81px"><span class="name">Breakfa</span></div>
      <div class="act" style="left:196px;width:57px;background:var(--mint);font-size:40px;font-weight:300">✕</div>
      <div class="act" style="left:258px;width:58px;background:var(--mint);font-size:34px">★</div>
      <div class="act" style="left:322px;width:58px;background:var(--mint)"></div>
      <div class="more">•••</div></div>
    <div class="row" style="top:128px"><div class="cell food" style="--line:var(--mint);width:211px"><span class="name">Apple</span><span class="qty">150 gr</span></div>
      <div class="act" style="left:216px;width:50px;background:var(--wine);font-size:40px;font-weight:300">✕</div>
      <div class="act" style="left:266px;width:5px;background:#8b95a6"></div>
      <div class="act" style="left:273px;width:55px;background:var(--gold);font-size:32px">★</div>
      <div class="act" style="left:333px;width:53px;background:#8a8a8a"></div>
      <div class="act" style="left:391px;width:54px;background:var(--crimson);font-size:20px;font-weight:700;letter-spacing:2px">•••</div></div>
    <div class="row" style="top:192px"><div class="cell blank"></div><div class="cell meal" style="--tag:var(--mint)"><span class="name">Mid-morning</span><span class="kcal">60<small>kcal</small></span></div>
      <div class="macros"><i class="p"><s>P:</s><b>10</b></i><i class="c"><s>C:</s><b>50</b></i><i class="f"><s>F:</s><b>35</b></i></div><div class="more">•••</div></div>
    <div class="row" style="top:256px"><div class="cell food" style="--line:var(--amber)"><span class="name">Cesar Salad</span><span class="qty">300 gr</span><span class="kcal">150<small>kcal</small></span></div>
      <div class="macros"><i class="p"><s>P:</s><b>10</b></i><i class="c"><s>C:</s><b>50</b></i><i class="f"><s>F:</s><b>35</b></i></div><div class="more">•••</div></div>
  </section>
  <div class="arrow" style="left:1180px;top:1134px;width:38px"></div>
  <div class="abs" style="left:1173px;top:1130px;border-top:5px solid transparent;border-bottom:5px solid transparent;border-right:8px solid var(--alert)"></div>
  <div class="arrow" style="left:1180px;top:1192px;width:38px"></div>
  <div class="abs" style="left:1173px;top:1188px;border-top:5px solid transparent;border-bottom:5px solid transparent;border-right:8px solid var(--alert)"></div>
</main>
</body>
</html>
```